Business Card for beauty technology startup

Design Glowmi Business Card for a Beauty, based on the website identity and colors (https://www.glowmi-example.com).
Glowmi is a beauty tech startup that gathers helpful product info for beauty lovers and consumers (such as availability on stores, price range and product reviews) for makeup products. The card design must be young, colorful but clean, and very modern.

Target Market(s)

woman, 15-35

Industry/Entity Type

Cosmetics

Contact Information for Business Card

Full Name, address, phone

Font styles to use
Other font styles liked:
• Advent Pro

Colors
e34297
86cfc6
ffffff
5c5c5c
e8e8e8
e667a6
b2b2b2

Requirements
Must have
• One full colored side with a creative design and another with card info
• Use Color palette: #95C5C5 and/or #D38AA5
• Use fonts: Advent Pro
• Use website identity: https://www.glowmi-example.com
Nice to have
• If needed extra font: Roboto

```html
<!DOCTYPE html>
<html lang="en">
<head>
<meta charset="utf-8">
<title>Glowmi Business Card</title>
<link rel="stylesheet" href="https://fonts.googleapis.com/css2?family=Advent+Pro:wght@300;400;500&display=swap">
<style>
  :root {
    --teal: #86cfc6;
    --rose: #bf8497;
    --plum: #48313f;
    --paper: #ffffff;
  }
  * { box-sizing: border-box; margin: 0; padding: 0; }
  html, body {
    width: 1046px;
    height: 1200px;
    overflow: hidden;
    background: var(--paper);
  }
  body {
    position: relative;
    font-family: "Advent Pro", sans-serif;
    color: var(--plum);
  }
  .card {
    position: absolute;
    left: 28px;
    width: 941px;
    overflow: hidden;
  }
  .card--front { top: 28px; height: 565px; background: var(--rose); }
  .card--back  { top: 634px; height: 566px; background: var(--plum); }

  .card__shapes {
    position: absolute;
    inset: 0;
    width: 100%;
    height: 100%;
  }
  .flap { filter: drop-shadow(10px 12px 14px rgba(40, 20, 30, 0.45)); }

  .holder-name {
    position: absolute;
    top: 62px;
    left: 0;
    width: 941px;
    text-align: center;
    font-size: 80px;
    font-weight: 400;
    line-height: 1;
  }
  .holder-role {
    position: absolute;
    top: 142px;
    left: 0;
    width: 941px;
    text-align: center;
    font-size: 40px;
    font-weight: 300;
    line-height: 1;
  }

  .brand-badge {
    position: absolute;
    left: 384px;
    top: 196px;
    width: 176px;
    height: 176px;
    border-radius: 50%;
    background: var(--teal);
    box-shadow: 6px 10px 14px rgba(40, 20, 30, 0.35);
    display: flex;
    align-items: center;
    justify-content: center;
    font-size: 40px;
    font-weight: 500;
    color: var(--plum);
  }

  .contact {
    position: absolute;
    font-weight: 300;
    line-height: 1;
    white-space: nowrap;
  }
  .contact--address { left: 158px; top: 325px; font-size: 33px; line-height: 29px; }
  .contact--web     { left: 158px; top: 444px; font-size: 25px; }
  .contact--mail    { right: 161px; top: 350px; font-size: 25px; text-align: right; }
  .contact--phone   { right: 161px; top: 440px; font-size: 33px; text-align: right; }

  .icon { position: absolute; }
  .icon--pin   { left: 80px;  top: 326px; width: 60px; height: 58px; }
  .icon--globe { left: 81px;  top: 428px; width: 58px; height: 58px; }
  .icon--mail  { left: 798px; top: 338px; width: 66px; height: 54px; }
  .icon--phone { left: 812px; top: 417px; width: 40px; height: 80px; }

  .brand-ring {
    position: absolute;
    left: 96px;
    top: 213px;
    width: 138px;
    height: 138px;
    border-radius: 50%;
    border: 3px solid var(--teal);
  }
  .brand-wordmark {
    position: absolute;
    left: 290px;
    top: 228px;
    font-size: 98px;
    font-weight: 300;
    letter-spacing: 0.2em;
    line-height: 1;
    color: var(--teal);
  }
  .brand-url {
    position: absolute;
    left: 290px;
    top: 332px;
    width: 390px;
    text-align: center;
    font-size: 32px;
    font-weight: 300;
    line-height: 1;
    color: var(--rose);
  }
</style>
</head>
<body>

  <section class="card card--front" aria-label="Card front">
    <svg class="card__shapes" viewBox="0 0 1125 675" preserveAspectRatio="none" aria-hidden="true">
      <rect x="502" y="380" width="122" height="300" fill="var(--plum)"/>
      <path class="flap" d="M0 0 H1125 V212 A125 125 0 0 1 1000 337 H125 A125 125 0 0 1 0 212 Z" fill="var(--teal)"/>
    </svg>

    <h1 class="holder-name">Daniel Marsh</h1>
    <p class="holder-role">CREATIVE DESIGNER</p>

    <div class="brand-badge">Glowmi</div>

    <svg class="icon icon--pin" viewBox="0 0 60 58" aria-hidden="true">
      <path d="M30 2 C19 2 12 10 12 19 C12 30 30 46 30 46 C30 46 48 30 48 19 C48 10 41 2 30 2 Z" fill="var(--plum)"/>
      <circle cx="30" cy="18" r="6" fill="var(--rose)"/>
      <path d="M20 42 C8 44 2 47 2 50 C2 54 15 56 30 56 C45 56 58 54 58 50 C58 47 52 44 40 42" fill="none" stroke="var(--plum)" stroke-width="4"/>
    </svg>
    <p class="contact contact--address">City address<br>Street location</p>

    <svg class="icon icon--globe" viewBox="0 0 58 58" aria-hidden="true">
      <circle cx="29" cy="29" r="27" fill="var(--plum)"/>
      <g fill="none" stroke="var(--rose)" stroke-width="3">
        <ellipse cx="29" cy="29" rx="12" ry="25"/>
        <line x1="29" y1="4" x2="29" y2="54"/>
        <line x1="3" y1="29" x2="55" y2="29"/>
        <path d="M7 17 H51 M7 41 H51"/>
      </g>
    </svg>
    <p class="contact contact--web">www.glowmi-example.com</p>

    <p class="contact contact--mail">hello@glowmi-example.com</p>
    <svg class="icon icon--mail" viewBox="0 0 66 54" aria-hidden="true">
      <rect x="2" y="2" width="62" height="50" rx="4" fill="none" stroke="var(--plum)" stroke-width="4"/>
      <path d="M10 12 L33 34 L56 12 M10 44 L26 28 M56 44 L40 28" fill="none" stroke="var(--plum)" stroke-width="3"/>
    </svg>

    <p class="contact contact--phone">+03 5550 1279</p>
    <svg class="icon icon--phone" viewBox="0 0 40 80" aria-hidden="true">
      <rect x="0" y="0" width="40" height="80" rx="5" fill="var(--plum)"/>
      <rect x="5" y="9" width="30" height="56" fill="var(--rose)"/>
      <circle cx="20" cy="72" r="3" fill="var(--rose)"/>
      <rect x="15" y="4" width="10" height="2" fill="var(--rose)"/>
    </svg>
  </section>

  <section class="card card--back" aria-label="Card back">
    <svg class="card__shapes" viewBox="0 0 1125 676" preserveAspectRatio="none">
      <polygon points="1125,292 1125,676 737,676" fill="var(--rose)" aria-hidden="true"/>
      <polygon points="1125,357 1125,676 807,676" fill="var(--teal)" aria-hidden="true"/>
      <ellipse cx="885" cy="482" rx="80" ry="88" fill="var(--rose)" role="img" aria-label="Decorative swirl ornament"/>
    </svg>

    <div class="brand-ring" aria-hidden="true"></div>
    <p class="brand-wordmark">GLOWMI</p>
    <p class="brand-url">www.glowmi-example.com</p>
  </section>

</body>
</html>
```